Local fast-growing company in the service sector

We are looking for a modern business card design, which should also appear on our letterheads

Target Market(s)

Private and industrial sectors

Contact Information for Business Card

Vorname Name
Lindkofer Str. 18
71468 Tannbrunn
Tel.: 07163-418259-0
Name@kovaltec-pbz.de

Colors
9d9d9d
919191
aaaaaa

Requirements
Must have
• The logo (file) in silver

```html
<!DOCTYPE html>
<html lang="de">
<head>
<meta charset="utf-8">
<title>KOVALTEC – Visitenkarte</title>
<link href="https://fonts.googleapis.com/css2?family=Open+Sans:wght@400;600&display=swap" rel="stylesheet">
<style>
  :root {
    --page: #ffffff;
    --card-light: #efefef;
    --card-mid: #d6d6d6;
    --panel: #f4f4f4;
    --brand: #9eabad;
    --text: #6c7c7e;
  }
  html, body {
    margin: 0;
    width: 1200px;
    height: 704px;
    overflow: hidden;
    background: var(--page);
    font-family: "Open Sans", sans-serif;
  }
  .card {
    position: absolute;
    left: 0;
    top: 37px;
    width: 1200px;
    height: 667px;
    border-radius: 36px 0 46px 0;
    overflow: hidden;
  }
  .card-texture {
    position: absolute;
    inset: 0;
    background:
      radial-gradient(ellipse 420px 210px at 600px 230px, rgba(90,90,90,0.55), rgba(90,90,90,0) 70%),
      linear-gradient(160deg, var(--card-light) 0%, var(--card-mid) 55%, var(--card-light) 100%);
  }
  .brand-panel {
    position: absolute;
    left: 195px;
    top: 28px;
    width: 827px;
    height: 308px;
    background: var(--panel);
    display: flex;
    flex-direction: column;
    align-items: center;
    justify-content: center;
    gap: 8px;
  }
  .brand-row {
    display: flex;
    align-items: center;
    gap: 34px;
  }
  .brand-mark {
    width: 70px;
    height: 70px;
    background: var(--brand);
  }
  .brand-name {
    font-size: 118px;
    font-weight: 600;
    line-height: 1;
    letter-spacing: 2px;
    color: var(--brand);
  }
  .brand-web {
    font-size: 44px;
    font-weight: 400;
    letter-spacing: 6px;
    color: var(--brand);
    line-height: 1;
  }
  .contact {
    position: absolute;
    left: 0;
    width: 1152px;
    top: 360px;
    margin: 0;
    text-align: center;
    font-size: 34px;
    line-height: 49.5px;
    font-style: normal;
    color: var(--text);
  }
</style>
</head>
<body>
  <div class="card">
    <div class="card-texture" role="img" aria-label="Hellgraues Dreiecksmuster mit weichem Schatten"></div>
    <div class="brand-panel">
      <div class="brand-row">
        <span class="brand-mark"></span>
        <span class="brand-name">KOVALTEC</span>
      </div>
      <span class="brand-web">kovaltec-pbz.de</span>
    </div>
    <address class="contact">
      Vorname Name<br>
      Lindkofer Str. 18<br>
      71468 Tannbrunn<br>
      Tel.: 07163-418259-0<br>
      Name@kovaltec-pbz.de
    </address>
  </div>
</body>
</html>
```